Refresh of The Marston Collective business card

Update business card design using existing primary logo. Names, numbers, etc. are too hard to read on current design.

Target Market(s)

We are a CPA firm.

Industry/Entity Type

Accountant

Contact Information for Business Card

update current card

Colors
0355a3
3176b5
85acd3
0792cd

Requirements
Must have
• Easier to read phone numbers and names
• Use existing logo
Nice to have
• We love our color scheme and current TMC logo. But the names and phone numbers are too small and card just look old and stale.

```html
<!DOCTYPE html>
<html lang="en">
<head>
<meta charset="utf-8">
<title>The Marston Collective — Business Card</title>
<link rel="stylesheet" href="https://fonts.googleapis.com/css2?family=Cinzel:wght@600&family=EB+Garamond:wght@500;600;700&family=Josefin+Sans:wght@600&display=swap">
<style>
  :root {
    --brand-deep: #0355a3;
    --brand-mid: #3176b5;
    --brand-light: #85acd3;
    --brand-bright: #0792cd;
    --navy-edge: #0b2f6b;
    --paper: #ffffff;
    --paper-shade: #eef1f5;
    --soft-white: #e8eef6;
    --backdrop: #262626;
    --ink-grey: #8a8f99;
  }
  * { box-sizing: border-box; margin: 0; padding: 0; }
  html, body {
    width: 1200px; height: 997px; overflow: hidden;
    background: var(--backdrop);
  }
  .stage { position: relative; width: 1200px; height: 997px; }

  .card {
    position: absolute; left: 250px; width: 700px; height: 400px;
    overflow: hidden; box-shadow: 0 10px 30px rgba(0,0,0,.5);
  }

  /* ---------- Front ---------- */
  .card--front { top: 70px; background: var(--paper); }
  .front__header {
    position: absolute; inset: 0 0 auto 0; height: 206px;
    background: linear-gradient(180deg, var(--paper), var(--paper-shade));
    display: flex; align-items: center; justify-content: center; gap: 26px;
  }
  .brand-dot {
    width: 96px; height: 96px; border-radius: 50%;
    background: var(--brand-deep);
    flex: none;
  }
  .brand-lockup { display: flex; flex-direction: column; align-items: flex-start; }
  .brand-name {
    font-family: "Cinzel", serif; font-weight: 600;
    font-size: 34px; line-height: 1.05; color: var(--brand-deep);
    letter-spacing: 1px; border-bottom: 1.5px solid var(--brand-light);
    padding-bottom: 6px;
  }
  .brand-tagline {
    font-family: "Josefin Sans", sans-serif; font-weight: 600;
    font-size: 11px; letter-spacing: 3.2px; text-transform: uppercase;
    color: var(--ink-grey); margin-top: 7px;
  }
  .front__rules {
    position: absolute; left: 0; right: 0; top: 206px; height: 18px;
    background:
      linear-gradient(var(--brand-mid), var(--brand-mid)) 0 2px / 100% 3px no-repeat,
      linear-gradient(var(--brand-mid), var(--brand-mid)) 0 8px / 100% 2px no-repeat,
      linear-gradient(var(--brand-mid), var(--brand-mid)) 0 13px / 100% 2px no-repeat;
  }
  .front__body {
    position: absolute; left: 0; right: 0; top: 224px; bottom: 0;
    background: linear-gradient(170deg, var(--brand-mid) 0%, var(--brand-deep) 70%);
    color: var(--paper);
  }
  .contact-list {
    position: absolute; left: 60px; top: 26px; list-style: none;
    font-family: "EB Garamond", serif; font-weight: 500; font-size: 21px;
  }
  .contact-list li { display: flex; align-items: center; gap: 14px; height: 32px; }
  .contact-list svg { width: 18px; height: 18px; flex: none; }
  .front__divider {
    position: absolute; left: 372px; top: 0; width: 1.5px; height: 110px;
    background: var(--brand-light);
  }
  .person {
    position: absolute; left: 400px; top: 18px;
    font-family: "EB Garamond", serif;
  }
  .person__name {
    font-weight: 700; font-size: 20px; letter-spacing: 1px;
    text-transform: uppercase; color: var(--paper);
  }
  .person__address { font-weight: 500; font-size: 17px; line-height: 1.35; margin-top: 14px; color: var(--soft-white); }

  /* ---------- Back ---------- */
  .card--back {
    top: 520px;
    background: radial-gradient(ellipse at 45% 40%, var(--brand-mid) 0%, var(--brand-deep) 45%, var(--navy-edge) 100%);
    color: var(--paper);
  }
  .back__halo {
    position: absolute; left: 50%; top: 40px; width: 300px; height: 300px;
    margin-left: -150px; border-radius: 50%;
    background: rgba(133,172,211,.16);
  }
  .back__lockup {
    position: absolute; left: 0; right: 0; top: 120px;
    display: flex; flex-direction: column; align-items: center;
  }
  .back__lockup .brand-name {
    color: var(--paper); font-size: 46px; border-bottom-color: rgba(255,255,255,.7);
    padding: 0 6px 8px;
  }
  .back__lockup .brand-tagline { color: var(--paper); font-size: 14px; letter-spacing: 4px; margin-top: 12px; }
  .back__web {
    position: absolute; left: 0; right: 0; top: 300px; text-align: center;
    font-family: "Josefin Sans", sans-serif; font-weight: 600;
    font-size: 19px; letter-spacing: 3px; color: var(--soft-white);
  }
</style>
</head>
<body>
<main class="stage">

  <section class="card card--front" aria-label="Business card front">
    <header class="front__header">
      <span class="brand-dot" aria-hidden="true"></span>
      <div class="brand-lockup">
        <span class="brand-name">The Marston Collective</span>
        <span class="brand-tagline">Certified Public Accountants</span>
      </div>
    </header>
    <div class="front__rules" aria-hidden="true"></div>
    <div class="front__body">
      <ul class="contact-list">
        <li>
          <svg viewBox="0 0 20 20" aria-label="Phone"><path fill="#fff" d="M3 7c0-2 3-4 7-4s7 2 7 4l-1 2-3-1v-2H7v2l-3 1zM6 10h8l2 6H4z"/></svg>
          555.214.7730
        </li>
        <li>
          <svg viewBox="0 0 20 20" aria-label="Fax"><path fill="#fff" d="M6 2h8v5H6zM3 8h14v7h-3v3H6v-3H3zM7 13v3h6v-3z"/></svg>
          555.214.7731
        </li>
        <li>
          <svg viewBox="0 0 20 20" aria-label="Mobile"><rect x="5" y="2" width="10" height="16" rx="1.5" fill="none" stroke="#fff" stroke-width="1.6"/></svg>
          555.306.1842
        </li>
        <li>
          <svg viewBox="0 0 20 20" aria-label="Email"><rect x="2" y="5" width="16" height="11" fill="#fff"/><path d="M2 5l8 6 8-6" fill="none" stroke="#0355a3" stroke-width="1.5"/></svg>
          dan@marstoncollective.com
        </li>
      </ul>
      <div class="front__divider" aria-hidden="true"></div>
      <div class="person">
        <p class="person__name">Daniel R. Marston, CPA</p>
        <p class="person__address">318 Linden Park Ave. Suite 104<br>Winter Haven, Florida 33880</p>
      </div>
    </div>
  </section>

  <section class="card card--back" aria-label="Business card back">
    <div class="back__halo" aria-hidden="true"></div>
    <div class="back__lockup">
      <span class="brand-name">The Marston Collective</span>
      <span class="brand-tagline">Certified Public Accountants</span>
    </div>
    <p class="back__web">www.marstoncollective.com</p>
  </section>

</main>
</body>
</html>
```